Business card for my company-RMK Design Studio

I do not have a logo-I like red and keeping it clean. Information that should be on the card:
Tom Brakefield AIA
Architecture Planning Interiors
Cell Phone-614.492.5068
email-rmkarchitect1@lunvale.com
www.rmkdesignstudio.net

```html
<!DOCTYPE html>
<html lang="en">
<head>
<meta charset="utf-8">
<title>RMK Design Studio – Business Card</title>
<link rel="stylesheet" href="https://fonts.googleapis.com/css2?family=Crimson+Text&family=Karla:wght@400&display=swap">
<style>
  :root {
    --backdrop: #9a9a9a;
    --card-dark: #222123;
    --card-light: #ffffff;
    --ink-light: #ffffff;
    --ink-dark: #1a1a1a;
  }
  * { margin: 0; padding: 0; box-sizing: border-box; }
  html, body {
    width: 1133px; height: 1200px; overflow: hidden;
    background: var(--backdrop);
  }
  .canvas { position: relative; width: 1133px; height: 1200px; }

  .card { position: absolute; width: 725px; height: 412px; overflow: hidden; }
  .card-front { left: 197px; top: 144px; display: flex; }
  .card-back { left: 202px; top: 640px; width: 719px; height: 411px; background: var(--card-dark); }

  .front-details {
    width: 352px; height: 100%;
    background: var(--card-dark);
    color: var(--ink-light);
    padding: 96px 0 0 49px;
    font-family: "Karla", Arial, sans-serif;
  }
  .person-name {
    font-family: "Crimson Text", Georgia, serif;
    font-size: 27px; font-weight: 400; line-height: 1;
    letter-spacing: 0.2px;
  }
  .person-role { font-size: 16.4px; margin-top: 5px; letter-spacing: 0.4px; }
  .address { font-size: 15px; line-height: 20.5px; margin-top: 24px; letter-spacing: 0.3px; font-style: normal; }
  .contact-list { list-style: none; margin-top: 15px; font-size: 15px; letter-spacing: 0.3px; }
  .contact-list li { display: flex; align-items: center; height: 20.5px; }
  .contact-list svg { width: 13px; height: 13px; margin-right: 9px; flex: none; fill: var(--ink-light); }

  .front-brand {
    flex: 1; height: 100%;
    background: var(--card-light);
    display: flex; align-items: center; justify-content: center;
    padding-bottom: 9px;
  }
  .studio-name {
    font-family: "Karla", Arial, sans-serif;
    font-weight: 400; white-space: nowrap;
    letter-spacing: 0.5px;
  }
  .front-brand .studio-name { font-size: 28px; color: var(--ink-dark); }
  .card-back {
    display: flex; align-items: center; justify-content: center;
  }
  .card-back .studio-name { font-size: 48px; color: var(--ink-light); padding-bottom: 12px; }
</style>
</head>
<body>
<main class="canvas">
  <section class="card card-front" aria-label="Card front">
    <div class="front-details">
      <h1 class="person-name">Tom Brakefield AIA</h1>
      <p class="person-role">Architecture Planning Interiors</p>
      <address class="address">418 Larkspur Ave.<br>#112 Marrow Bay,<br>Ohio 43219</address>
      <ul class="contact-list">
        <li>
          <svg viewBox="0 0 16 16" aria-hidden="true"><path d="M3.6 1.2l2.3-.4 1.4 3.4-1.6 1.3c.8 1.8 2.1 3.1 3.9 3.9l1.3-1.6 3.4 1.4-.4 2.3c-.2.9-1 1.5-1.9 1.4C6.6 12.4 2.9 8.7 2.2 3.1c-.1-.9.5-1.7 1.4-1.9z"/></svg>
          614.492.5068
        </li>
        <li>
          <svg viewBox="0 0 16 16" aria-hidden="true"><path d="M1 4h14v9H1z" /><path d="M1.5 4.5L8 9l6.5-4.5" fill="none" stroke="#222123" stroke-width="1.3"/></svg>
          rmkarchitect1@lunvale.com
        </li>
        <li>
          <svg viewBox="0 0 16 16" aria-hidden="true"><circle cx="8" cy="8" r="7"/><path d="M4 5.5c1.5-.5 2.5 1 2 2.2-.4 1 1 1.8.4 3.3M10 3.5c-.5 1.3.8 2 2 1.8M9.5 12.5c.3-1.3 1.6-1.6 2.6-1.2" fill="none" stroke="#222123" stroke-width="1.2"/></svg>
          www.rmkdesignstudio.net
        </li>
      </ul>
    </div>
    <div class="front-brand">
      <p class="studio-name">RMK Design Studio</p>
    </div>
  </section>

  <section class="card card-back" aria-label="Card back">
    <p class="studio-name">RMK Design Studio</p>
  </section>
</main>
</body>
</html>
```